Halvern Structural Approval Standards Private Assessors

Professional Construction Consultancy Company Business Card - must keep logo colours see images below - examples have been added from my last competition - please see them as examples only!

Target Market(s)

Home Builders

Industry/Entity Type

Construction

Contact Information for Business Card

See "must haves"

Font styles to use
Sans Serif

Colors
ffffff
add136
000000

Requirements
Must have
• Daniel Moravi
• Director
• Phone: 0431 587 219
• Address: 7 Tarrunga Rd,
• Hallworth Vale, SA, 5091
• Email: halvern@mailbox-example.com
• Website: www.halvern-example.com.au
• Facebook: Halvern Structural Approval Standards
Nice to have
• Side 1: full logo
• Side 2: company details
Should not have
• hard to read
• must be clear and professional

```html
<!DOCTYPE html>
<html lang="en">
<head>
<meta charset="utf-8">
<title>Halvern Structural Approval Standards – Business Card</title>
<link href="https://fonts.googleapis.com/css2?family=Lato:wght@400;700;900&display=swap" rel="stylesheet">
<style>
  :root {
    --backdrop: #252525;
    --card: #ffffff;
    --green: #add136;
    --ink: #000000;
    --rule: #222222;
  }
  html, body {
    margin: 0;
    padding: 0;
    width: 1189px;
    height: 1200px;
    overflow: hidden;
    background: var(--backdrop);
    font-family: "Lato", Arial, sans-serif;
  }
  .canvas {
    position: relative;
    width: 1189px;
    height: 1200px;
  }
  .card {
    position: absolute;
    left: 171px;
    width: 855px;
    height: 488px;
    background: var(--card);
    border-radius: 26px;
  }
  .card--front { top: 67px; }
  .card--back  { top: 626px; }

  .wordmark {
    position: absolute;
    display: flex;
    align-items: flex-start;
    color: var(--green);
    font-weight: 900;
    text-transform: uppercase;
    line-height: 1.05;
    white-space: nowrap;
  }
  .wordmark__square {
    flex: none;
    background: var(--green);
  }
  .card--front .wordmark {
    left: 176px;
    top: 170px;
    font-size: 38px;
    gap: 22px;
  }
  .card--front .wordmark__square { width: 118px; height: 118px; margin-top: 4px; }
  .card--back .wordmark {
    left: 40px;
    top: 188px;
    font-size: 24px;
    gap: 14px;
  }
  .card--back .wordmark__square { width: 74px; height: 74px; margin-top: 3px; }

  .divider {
    position: absolute;
    left: 425px;
    top: 107px;
    width: 1.5px;
    height: 269px;
    background: var(--rule);
  }
  .details {
    position: absolute;
    left: 461px;
    top: 110px;
    color: var(--ink);
  }
  .details__name {
    margin: 0;
    font-size: 30px;
    font-weight: 900;
    line-height: 1;
    text-transform: uppercase;
  }
  .details__role {
    margin: 2px 0 0;
    font-size: 23px;
    color: var(--green);
  }
  .details__address {
    margin: 22px 0 0;
    font-style: normal;
    font-size: 24px;
    line-height: 1.3;
  }
  .contacts {
    list-style: none;
    margin: 18px 0 0;
    padding: 0;
    font-size: 21px;
  }
  .contacts li {
    display: flex;
    align-items: center;
    gap: 6px;
    height: 29px;
    white-space: nowrap;
  }
  .contacts svg {
    flex: none;
    width: 26px;
    height: 26px;
  }
</style>
</head>
<body>
<div class="canvas">

  <section class="card card--front" aria-label="Card front">
    <div class="wordmark">
      <span class="wordmark__square"></span>
      <span>Halvern Structural<br>Approval Standards<br>Private Assessors</span>
    </div>
  </section>

  <section class="card card--back" aria-label="Card back">
    <div class="wordmark">
      <span class="wordmark__square"></span>
      <span>Halvern Structural<br>Approval Standards<br>Private Assessors</span>
    </div>

    <div class="divider"></div>

    <div class="details">
      <h1 class="details__name">Daniel Moravi</h1>
      <p class="details__role">Director</p>
      <address class="details__address">7 Tarrunga Rd,<br>Hallworth Vale, SA, 5091</address>
      <ul class="contacts">
        <li>
          <svg viewBox="0 0 26 26" aria-hidden="true"><rect width="26" height="26" rx="3" fill="#add136"/><path d="M8 6c1-1 2-1 3 0l1 3c0 1-1 1-1 2 1 2 2 3 4 4 1 0 1-1 2-1l3 1c1 1 1 2 0 3-2 2-5 1-8-2s-5-7-4-10z" fill="#fff"/></svg>
          <span>0431 587 219</span>
        </li>
        <li>
          <svg viewBox="0 0 26 26" aria-hidden="true"><rect width="26" height="26" rx="3" fill="#add136"/><rect x="5" y="8" width="16" height="11" fill="none" stroke="#fff" stroke-width="1.6"/><path d="M5 8l8 6 8-6" fill="none" stroke="#fff" stroke-width="1.6"/></svg>
          <span>halvern@mailbox-example.com</span>
        </li>
        <li>
          <svg viewBox="0 0 26 26" aria-hidden="true"><rect width="26" height="26" rx="3" fill="#add136"/><g fill="none" stroke="#fff" stroke-width="1.4"><circle cx="13" cy="13" r="8"/><ellipse cx="13" cy="13" rx="3.5" ry="8"/><path d="M5 13h16M6.5 9h13M6.5 17h13"/></g></svg>
          <span>www.halvern-example.com.au</span>
        </li>
        <li>
          <svg viewBox="0 0 26 26" aria-hidden="true"><rect width="26" height="26" rx="3" fill="#add136"/></svg>
          <span>Halvern Structural Approval Standards</span>
        </li>
      </ul>
    </div>
  </section>

</div>
</body>
</html>
```